依頼詳細
■概要
会社の新規設立に伴い名刺のデザインの作成を依頼致します。

■パターン
A.日本語のみ
B.英語のみ
C.日本語と英語両方
それぞれをにおけるデザインを依頼します

記載項目
表面:会社名、住所、電話番号、役職、Mail、名前
裏面:会社のロゴ(マークのみORマーク+文字)
希望イメージ
シンプル 複雑
単色 カラフル
暗い 明るい
日常 高級
遊び心 厳粛
未来的 伝統的
女性的 男性的
納品ファイル
• 高解像度JPG (.jpg)
• イラストレーター形式 (.ai)
• PNG形式 (.png)
補足説明
皆様

多数のご提案頂き誠にありがとうございます。

本件依頼の補足になります。

□シンプルさ
・デザインは表面、裏面ともに極力シンプルなものでお願い致します。

□裏面のデザインについて
・会社ロゴのマークの部分のみ(文字なし)のデザインを推奨致します。
・マークは小さく、派手にならないような形にてお願い致します。
期限を延長させていただきます。

引き続き、ご提案お待ちしております。
■ 選んだ理由

必要な情報をシンプルに盛り込んでいただきました。
全体のバランスや、デザインのアクセントなど、非常に素敵なご提案を頂きました。
また、途中の質問等に対して、真摯かつ迅速にご対応頂いたこと、感謝しております。

■ 提案者全員のお礼・コメント

素敵なご提案を多数頂き、誠にありがとうございました!

```html
<!DOCTYPE html>
<html lang="en">
<head>
<meta charset="utf-8">
<title>veltora business card — front</title>
<link rel="stylesheet" href="https://fonts.googleapis.com/css2?family=Arimo:wght@400&display=swap">
<style>
  :root {
    --page-bg: #e9ebee;
    --card-bg: #ffffff;
    --brand-blue: #2a6db5;
    --wordmark-grey: #a3a3a3;
    --info-grey: #9a9a9a;
    --name-grey: #555555;
  }
  html, body {
    margin: 0;
    padding: 0;
    width: 1200px;
    height: 1200px;
    overflow: hidden;
    background: var(--page-bg);
  }
  .canvas {
    position: relative;
    width: 1200px;
    height: 1200px;
  }
  .business-card {
    position: absolute;
    left: 54px;
    top: 270px;
    width: 1092px;
    height: 660px;
    background: var(--card-bg);
  }
  .card-content {
    position: absolute;
    left: 222px;
    top: 196px;
    width: 650px;
    font-family: "Arimo", Arial, sans-serif;
    color: var(--info-grey);
  }
  .brand-row {
    display: flex;
    align-items: flex-end;
    gap: 30px;
    height: 128px;
  }
  .brand-square {
    flex: none;
    width: 118px;
    height: 118px;
    background: var(--brand-blue);
    margin-bottom: 4px;
  }
  .brand-name {
    font-family: "Arimo", Arial, sans-serif;
    font-weight: 400;
    font-size: 128px;
    line-height: 0.9;
    color: var(--wordmark-grey);
  }
  .info-row {
    display: flex;
    justify-content: space-between;
    align-items: baseline;
    font-size: 21px;
    line-height: 1;
    white-space: nowrap;
  }
  .info-row.identity { margin-top: 26px; }
  .info-row.address { margin-top: 12px; }
  .info-row.contact { margin-top: 11px; }
  .address-text {
    display: block;
    width: 100%;
    text-align: justify;
    text-align-last: justify;
  }
  .person-title { font-size: 21px; margin-right: 8px; }
  .person-name { font-size: 28px; color: var(--name-grey); }
</style>
</head>
<body>
  <main class="canvas">
    <section class="business-card" aria-label="Business card front">
      <div class="card-content">
        <div class="brand-row">
          <span class="brand-square" aria-hidden="true"></span>
          <span class="brand-name">veltora</span>
        </div>
        <div class="info-row identity">
          <span class="company-name">veltora, Inc.</span>
          <span class="person"><span class="person-title">President</span><span class="person-name">Kenji Morita</span></span>
        </div>
        <div class="info-row address">
          <span class="address-text">3F, KMBld, 4-5-6, Ebisu, Shibuya-ku 150-0013 Japan</span>
        </div>
        <div class="info-row contact">
          <span>Tel. +81-3-5550-0192</span>
          <span>E-mail. k.morita@veltora.com</span>
        </div>
      </div>
    </section>
  </main>
</body>
</html>
```